PebbleTrustLending.com

We are setting up a new company to make small business loans over the internet. We have a logo. Customers will apply on line, so the online application must allow customers to upload files.

We need a complete design and also a some who can build the online application and website for us (CODING). When applicants fill out fields, at various points they may be able to move to the next questions or receive a notice that their application is not eligible for funding.

Sample sites are: MarbleHarbor.com/us, RovenTide.com, Quillory.com, ByNest.com, JuvaCredit.com, plumebridge.com, tollivan.com.

We think WordPress makes the most sense but we are open to suggestions.

Note, we will request that the winning designer build the site for us including the online application. We will negotiate this separately, I presume, before we pick the final winner.

Target Market(s)

Small businesses in the United States.

Industry/Entity Type

Small Business

Requirements
Must have
• Online application - fields and ability to upload basic files.

https://filevault.example-share.net/redir?resid=A48D2EF7C1B0E93!51827&authkey=!QZtRmW284pXkvNe&ithint=file,.pdf

```html
<!DOCTYPE html>
<html lang="en">
<head>
<meta charset="utf-8">
<title>PebbleTrustLending – Small Business Loans</title>
<link rel="stylesheet" href="https://fonts.googleapis.com/css2?family=Montserrat:wght@400;500;600;700&family=Raleway:wght@400;500&display=swap">
<style>
:root{
  --teal:#1b6581;
  --teal-dark:#174f66;
  --orange:#fb5a15;
  --text:#555;
  --muted:#888;
  --band:#f5f5f5;
  --line:#e4e4e4;
  --white:#fff;
}
*{margin:0;padding:0;box-sizing:border-box}
html,body{width:768px;height:1200px;overflow:hidden;background:var(--white)}
body{position:relative;font-family:"Raleway",Arial,sans-serif;color:var(--text)}
.abs{position:absolute}
.heading{font-family:"Montserrat",Arial,sans-serif}

.topbar{left:0;top:0;width:768px;height:27px;background:#f7f7f7;font-size:9px}
.topbar .call{position:absolute;right:132px;top:9px;color:#444}
.topbar .signin{position:absolute;left:643px;top:8px;color:var(--teal);font-family:"Montserrat",sans-serif;font-weight:600;font-size:9px;border-left:1px solid #bbb;padding-left:4px}

.header{left:0;top:27px;width:768px;height:56px;background:var(--white)}
.logo{position:absolute;left:77px;top:11px;display:flex;align-items:center;gap:6px}
.logo-dot{width:32px;height:32px;border-radius:50%;background:var(--orange)}
.logo-name{font-family:"Montserrat",sans-serif;font-weight:600;font-size:16px;color:var(--teal)}
.nav{position:absolute;top:23px;font-family:"Montserrat",sans-serif;font-weight:600;font-size:11px;color:var(--teal)}
.nav.active{color:var(--orange)}
.nav-apply{position:absolute;left:607px;top:19px;width:74px;height:22px;background:var(--teal-dark);color:var(--white);font-family:"Montserrat",sans-serif;font-weight:600;font-size:8.5px;display:flex;align-items:center;justify-content:center;letter-spacing:.3px}

.hero{left:0;top:83px;width:768px;height:315px;background:linear-gradient(120deg,#dfeaf0 0%,#eef2f4 35%,#e6c8b8 58%,#cfd7dd 75%,#3fb3c1 100%)}
.hero-title{position:absolute;left:94px;top:100px;font-family:"Montserrat",sans-serif;font-weight:600;font-size:21px;line-height:24px;color:var(--teal)}
.hero-btn{position:absolute;left:94px;top:155px;width:128px;height:36px;background:var(--orange);color:var(--white);font-family:"Montserrat",sans-serif;font-weight:600;font-size:14px;display:flex;align-items:center;justify-content:center;letter-spacing:.5px}
.dots{position:absolute;left:352px;top:286px;display:flex;gap:4px}
.dots span{width:13px;height:13px;border-radius:50%;background:var(--teal)}
.dots span:first-child{background:var(--orange)}

.press{left:0;top:398px;width:768px;height:60px;display:flex;align-items:center;justify-content:center;gap:22px;border-bottom:1px solid var(--line)}
.press span{color:#333;font-family:"Raleway",serif;font-size:10px;font-weight:500}

.features{left:0;top:458px;width:768px;height:236px;background:var(--band)}
.feature{position:absolute;top:20px;width:200px;text-align:center}
.feature .circle{width:114px;height:114px;border-radius:50%;background:var(--orange);margin:0 auto;display:flex;align-items:center;justify-content:center}
.feature h3{font-family:"Montserrat",sans-serif;font-weight:600;font-size:12px;color:var(--teal);margin-top:11px}
.feature p{font-size:9.2px;line-height:15.5px;margin-top:11px;color:var(--text)}

.how-title{left:0;top:715px;width:768px;text-align:center;font-family:"Montserrat",sans-serif;font-weight:600;font-size:19px;color:var(--teal)}
.video{left:83px;top:758px;width:344px;height:192px;border:1px solid var(--line);background:var(--white)}
.video-art{position:absolute;left:8px;top:8px;width:326px;height:174px;background:linear-gradient(135deg,#f4f4f4,#e9eef1)}
.video-play{position:absolute;left:147px;top:69px;width:53px;height:32px;background:#3a3a3a;border-radius:3px}
.video-bar{position:absolute;left:9px;top:151px;width:328px;height:22px;background:#3d3f42;border-radius:3px}
.video-track{position:absolute;left:6px;top:7px;width:240px;height:7px;border:1px solid #777;background:#555}
.video-fill{position:absolute;left:0;top:0;width:68px;height:100%;background:#1f8fd2}
.how-text{left:446px;top:766px;width:246px;font-size:9.1px;line-height:15.4px;color:var(--text)}
.get-started{left:445px;top:918px;width:107px;height:32px;background:var(--orange);color:var(--white);font-family:"Montserrat",sans-serif;font-weight:600;font-size:11px;display:flex;align-items:center;justify-content:center;letter-spacing:.5px}

.subscribe{left:112px;top:971px;width:602px;height:53px;border:1px solid #eee;background:var(--white)}
.sub-label{left:98px;top:989px;font-family:"Montserrat",sans-serif;font-size:11.5px;color:var(--teal)}
.sub-input{left:336px;top:985px;width:260px;height:26px;font-size:9px;color:#aaa;padding:8px 7px}
.sub-btn{left:597px;top:985px;width:75px;height:26px;background:var(--orange);color:var(--white);font-family:"Montserrat",sans-serif;font-weight:600;font-size:9.5px;display:flex;align-items:center;justify-content:center}

.footer{left:0;top:1040px;width:768px;height:160px;background:var(--band)}
.fcol{position:absolute;top:22px}
.fcol h4{font-family:"Montserrat",sans-serif;font-weight:600;font-size:8.5px;color:var(--teal);margin-bottom:13px}
.fcol li{list-style:none;font-size:9px;line-height:15.4px;color:var(--text)}
.badges{display:flex;gap:14px;align-items:center;margin-top:4px}
.badge-round{width:46px;height:46px;border-radius:50%;background:#1d4f8f}
.badge-rect{width:32px;height:50px;border-radius:3px;background:#1c5c9a}
.badge-tri{width:44px;height:46px}
.social li{display:flex;justify-content:space-between;width:88px;line-height:24px;align-items:center}
.social .ico{width:18px;height:18px;border-radius:50%;background:var(--orange)}
.copy{left:0;top:1173px;width:768px;text-align:center;font-size:8.5px;color:var(--text)}
</style>
</head>
<body>

<div class="abs topbar">
  <span class="call">Call Us: (800) 555-0142</span>
  <span class="signin">Sign In</span>
</div>

<header class="abs header">
  <div class="logo"><span class="logo-dot"></span><span class="logo-name">PebbleTrustLending</span></div>
  <span class="nav active" style="left:299px">Home</span>
  <span class="nav" style="left:352px">Our Business Loans</span>
  <span class="nav" style="left:475px">About Us</span>
  <span class="nav" style="left:539px">Contact Us</span>
  <span class="nav-apply">APPLY NOW</span>
</header>

<section class="abs hero" role="img" aria-label="Photo of hands typing on a laptop keyboard">
  <h1 class="hero-title">We give small business<br>loans over the internet.</h1>
  <span class="hero-btn">APPLY NOW</span>
  <div class="dots"><span></span><span></span><span></span><span></span></div>
</section>

<section class="abs press">
  <span>Westbay Commerce Journal</span>
  <span>Ledgerly</span>
  <span>Channel Nine</span>
  <span>Market Courier</span>
  <span>Startup Wire</span>
  <span>Harbor City Times</span>
</section>

<section class="abs features">
  <div class="feature" style="left:80px">
    <div class="circle">
      <svg width="42" height="38" viewBox="0 0 42 38"><rect x="1" y="1" width="40" height="26" rx="3" fill="#fff"/><rect x="5" y="5" width="32" height="16" fill="#fb5a15"/><rect x="18" y="27" width="6" height="6" fill="#fff"/><rect x="12" y="33" width="18" height="3" fill="#fff"/></svg>
    </div>
    <h3>Its Easy to Access</h3>
    <p>Sed ut perspiciatis unde omnis iste natus error sit voluptatem accusantium doloremque laudantium,</p>
  </div>
  <div class="feature" style="left:284px">
    <div class="circle">
      <svg width="36" height="46" viewBox="0 0 36 46"><path d="M9 26 L3 42 L10 39 L13 45 L18 30 Z M27 26 L33 42 L26 39 L23 45 L18 30 Z" fill="#fff"/><circle cx="18" cy="16" r="15" fill="#fff"/><text x="18" y="22" text-anchor="middle" font-family="Montserrat,sans-serif" font-weight="700" font-size="16" fill="#fb5a15">1</text></svg>
    </div>
    <h3>100% Guaranteed Loan</h3>
    <p>Sed ut perspiciatis unde omnis iste natus error sit voluptatem accusantium doloremque laudantium,</p>
  </div>
  <div class="feature" style="left:486px">
    <div class="circle">
      <svg width="44" height="36" viewBox="0 0 44 36"><rect x="2" y="11" width="8" height="12" fill="#fff"/><path d="M11 11 L36 2 L36 32 L11 23 Z" fill="#fff"/><rect x="38" y="13" width="4" height="8" fill="#fff"/><path d="M12 24 L18 24 L20 34 L15 34 Z" fill="#fff"/></svg>
    </div>
    <h3>24x7 Customer Support</h3>
    <p>Sed ut perspiciatis unde omnis iste natus error sit voluptatem accusantium doloremque laudantium,</p>
  </div>
</section>

<h2 class="abs how-title">How It Works</h2>

<div class="abs video">
  <div class="video-art" role="img" aria-label="Explainer video still with a cartoon character holding a tablet"></div>
  <div class="video-play"><svg width="53" height="32" viewBox="0 0 53 32"><path d="M21 9 L34 16 L21 23 Z" fill="#fff"/></svg></div>
  <div class="video-bar"><div class="video-track"><div class="video-fill"></div></div></div>
</div>

<p class="abs how-text">Sed ut perspiciatis unde omnis iste natus error sit voluptatem accusantium doloremque laudantium, totam rem aperiam, eaque ipsa quae ab illo inventore veritatis et quasi architecto beatae vitae dicta sunt explicabo. Nemo enim ipsam voluptatem quia voluptas sit aspernatur aut odit aut fugit, sed quia consequuntur magni dolores eos qui ratione voluptatem sequi nesciunt. Neque porro quisquam est, qui dolorem ipsum quia dolor sit amet, consectetur .</p>
<span class="abs get-started">GET STARTED</span>

<div class="abs subscribe"></div>
<span class="abs sub-label">Get Updated Mails From. Business Loans</span>
<span class="abs sub-input">E-Mail Address</span>
<span class="abs sub-btn">SUBSCRIBE</span>

<footer class="abs footer">
  <div class="fcol" style="left:98px">
    <h4>Quick Links</h4>
    <ul><li>Home</li><li>About Us</li><li>Our Business Loans</li><li>Contact Us</li></ul>
  </div>
  <div class="fcol" style="left:253px">
    <h4>Support Links</h4>
    <ul><li>Legal Notice</li><li>Privacy Policy</li><li>Terms &amp; Conditions</li><li>Help</li></ul>
  </div>
  <div class="fcol" style="left:388px">
    <h4 style="margin-left:6px">Accredited Logos</h4>
    <div class="badges">
      <span class="badge-round"></span>
      <span class="badge-rect"></span>
      <svg class="badge-tri" viewBox="0 0 44 46"><path d="M22 2 L42 44 L2 44 Z" fill="#f07a2a"/></svg>
    </div>
  </div>
  <div class="fcol social" style="left:596px">
    <h4>Connect With Us</h4>
    <ul><li>Chirpline<span class="ico"></span></li><li>Friendspace<span class="ico"></span></li><li>Worklink<span class="ico"></span></li></ul>
  </div>
</footer>
<p class="abs copy">Copyright ©2013 Company Name &nbsp;- All rights reserved</p>

</body>
</html>
```